Landing page для Landing-page для Salvira
Название сайта (домена, или проекта)
Landing-page для Salvira
Компания занимается производством и оптовой торговлей одноразовыми медицинскими и пищевыми расходными материалами.
Сайт ориентирован на закупщиков/собственников оптовых торгующих компаний, медицинских клиник, салонов красоты, пищевых производств, производственных предприятий.
Ссылка на скачивание брифа: https://filebox-drop.example/i/kQw7RmZp2VbXs8
Ссылка на скачивание бренд-бука: https://filebox-drop.example/i/HnLp4WtsY9cGfA
Ссылка на скачивание фото для каталога: https://filebox-drop.example/d/Bm2ruXkaQ7JdPe
Ссылка на скачивание векторного логотипа: https://filebox-drop.example/d/F-ZWNhuL8TsyKo
Адаптивность сайта
Десктопная версия, Версия для планшетов, Версия для телефонов

```html
<!DOCTYPE html>
<html lang="ru">
<head>
<meta charset="utf-8">
<title>Salvira — одноразовые медицинские расходные материалы</title>
<link rel="stylesheet" href="https://fonts.googleapis.com/css2?family=Roboto+Condensed:wght@400;700&family=Roboto:wght@400;500&display=swap">
<style>
  :root {
    --page-bg: #ffffff;
    --ink: #3a3a3a;
    --muted: #7a7a7a;
    --line: #e3e3e3;
    --brand-blue: #2b5c9e;
    --brand-red: #c3283c;
    --brand-green: #2ea64e;
    --logo-purple: #8d2a7a;
    --hero-blue: #2f5f96;
    --hero-teal: #3f8f86;
    --photo-light: #e9f1f5;
    --photo-gown: #a9d3e6;
  }
  * { box-sizing: border-box; margin: 0; padding: 0; }
  html, body { width: 1200px; height: 800px; overflow: hidden; background: var(--page-bg); }
  body { font-family: "Roboto", Arial, sans-serif; color: var(--ink); }

  .site-header {
    height: 92px; display: flex; align-items: center;
    padding: 0 70px; border-bottom: 1px solid var(--line);
  }
  .logo { display: flex; align-items: center; gap: 10px; width: 360px; }
  .logo-dot { width: 14px; height: 14px; border-radius: 50%; background: var(--logo-purple); }
  .logo-name {
    font-family: "Roboto Condensed", Arial, sans-serif; font-weight: 700;
    font-size: 34px; color: var(--logo-purple); letter-spacing: 1px;
  }
  .header-address { flex: 1; text-align: center; font-size: 12px; line-height: 1.5; color: var(--muted); }
  .header-contacts { width: 260px; font-size: 12px; line-height: 1.5; color: var(--muted); }
  .header-contacts strong { color: var(--ink); font-weight: 500; }

  .main-nav {
    height: 52px; display: flex; justify-content: center; align-items: center; gap: 34px;
    border-bottom: 1px solid var(--line);
  }
  .main-nav a { font-size: 13px; color: var(--ink); text-decoration: none; }

  .hero {
    position: relative; height: 656px;
    background: linear-gradient(135deg, var(--hero-blue) 0%, #336e8f 55%, var(--hero-teal) 100%);
  }
  .hero-card {
    position: absolute; left: 190px; top: 40px; width: 760px; height: 560px;
    background: #ffffff; display: flex; overflow: hidden;
  }
  .hero-photo {
    width: 320px; height: 100%;
    background: linear-gradient(180deg, var(--photo-light) 0%, var(--photo-gown) 100%);
  }
  .hero-content { flex: 1; padding: 70px 40px 0 30px; text-align: right; position: relative; }
  .hero-title {
    font-family: "Roboto Condensed", Arial, sans-serif; font-weight: 700;
    font-size: 31px; line-height: 1.22; color: var(--brand-blue); text-transform: uppercase;
  }
  .hero-rule { height: 2px; background: var(--brand-red); margin: 56px 0 22px; }
  .hero-lead {
    font-family: "Roboto Condensed", Arial, sans-serif; font-size: 18px; line-height: 1.3;
    color: var(--brand-red); text-transform: uppercase;
  }
  .hero-button {
    display: inline-block; margin-top: 42px; padding: 14px 24px;
    background: var(--brand-green); color: #fff; text-decoration: none;
    font-family: "Roboto Condensed", Arial, sans-serif; font-weight: 700; font-size: 14px;
    text-transform: uppercase;
  }
  .slider-dots { position: absolute; right: 40px; bottom: 28px; display: flex; gap: 6px; }
  .slider-dots span { width: 8px; height: 8px; border-radius: 50%; background: #b9c6d6; }
  .slider-dots span.is-active { background: var(--brand-blue); }

  .promo-tab {
    position: absolute; right: 180px; top: 40px; width: 40px; height: 230px;
    background: var(--brand-red); display: flex; align-items: center; justify-content: center;
  }
  .promo-tab span {
    writing-mode: vertical-rl; color: #fff; font-size: 12px; font-weight: 500;
    letter-spacing: 1px; text-transform: uppercase;
  }
</style>
</head>
<body>
  <header class="site-header">
    <div class="logo"><span class="logo-dot"></span><span class="logo-name">Salvira</span></div>
    <div class="header-address">г. Санкт-Петербург<br>ул. Садовая, д. 14, стр. 2</div>
    <div class="header-contacts"><strong>Тел.:</strong> 8 (800) 000-00-00<br><strong>E-mail:</strong> info@salvira.example</div>
  </header>

  <nav class="main-nav">
    <a href="#">Акции</a>
    <a href="#">О нас</a>
    <a href="#">Производство</a>
    <a href="#">С кем мы работаем</a>
    <a href="#">Каталог</a>
    <a href="#">Сертификаты</a>
    <a href="#">Наша команда</a>
    <a href="#">Отзывы о нас</a>
    <a href="#">Контакты</a>
  </nav>

  <section class="hero">
    <div class="hero-card">
      <div class="hero-photo" role="img" aria-label="Фото: медицинский работник в одноразовом халате, шапочке, маске и перчатках в светлой клинике"></div>
      <div class="hero-content">
        <h1 class="hero-title">Широкий ассортимент<br>качественных одноразовых<br>медицинских расходных материалов</h1>
        <div class="hero-rule"></div>
        <p class="hero-lead">Наша компания является надежным и<br>проверенным партнером с многолетней историей</p>
        <a class="hero-button" href="#">Перейти в каталог</a>
        <div class="slider-dots"><span class="is-active"></span><span></span><span></span></div>
      </div>
    </div>
    <a class="promo-tab" href="#"><span>Акции и скидки</span></a>
  </section>
</body>
</html>
```